Business Card Design for School

We need business cards for our school in Algiers, Algeria.
Our school is a Halvorth Quenby approved centre. (See P2 of attached file).
Our school name is "Ecole Les Bintal" in French and "Bintal School" in English.
We want two-sided cards—one side in English and the other in French.
We want both our school logo and the Halvorth Quenby "approved centre" logo on the cards.
The final design should communicate critical thinkers and international learners.
Thank you.
Name, Function, Phone number, Email address and website URL

```html
<!DOCTYPE html>
<html lang="fr">
<head>
<meta charset="utf-8">
<title>Ecole Les Bintal — Cartes de visite</title>
<link rel="stylesheet" href="https://fonts.googleapis.com/css2?family=Montserrat:wght@400;500;600;700&display=swap">
<style>
  :root {
    --navy: #002b55;
    --blue: #0e5a8a;
    --orange: #f26a21;
    --ink: #222222;
    --rule: #bdbdbd;
    --paper: #ffffff;
    --backdrop: #3a3a3a;
  }
  * { box-sizing: border-box; margin: 0; padding: 0; }
  html, body {
    width: 1200px; height: 1015px; overflow: hidden;
    background: var(--backdrop);
    font-family: "Montserrat", sans-serif;
  }
  .sheet {
    width: 1200px; height: 1015px;
    display: flex; flex-direction: column; align-items: center; justify-content: center;
    gap: 40px;
  }
  .card {
    position: relative;
    width: 840px; height: 440px;
    background: var(--paper);
    overflow: hidden;
    box-shadow: 0 10px 30px rgba(0,0,0,.45);
  }
  .card__band {
    position: absolute; left: 0; right: 0; bottom: 0; height: 78px;
    background: var(--navy);
  }
  .brand {
    position: absolute; left: 70px; top: 120px; width: 320px;
  }
  .brand__mark {
    display: flex; align-items: center; gap: 18px;
  }
  .brand__dot {
    width: 110px; height: 110px; border-radius: 50%;
    background: var(--orange); flex: none;
  }
  .brand__name {
    font-size: 46px; font-weight: 600; color: var(--blue); letter-spacing: 1px;
  }
  .brand__school {
    margin-top: 30px;
    font-size: 31px; font-weight: 600; color: var(--blue);
    text-transform: uppercase; letter-spacing: 1px; white-space: nowrap;
  }
  .card__divider {
    position: absolute; left: 420px; top: 70px; width: 1px; height: 230px;
    background: var(--rule);
  }
  .contact {
    position: absolute; left: 455px; top: 72px; width: 370px; color: var(--ink);
  }
  .contact__name {
    font-size: 28px; font-weight: 700; color: var(--blue); text-transform: uppercase; line-height: 1;
  }
  .contact__title {
    font-size: 19px; font-weight: 500; color: var(--orange); margin-top: 4px;
  }
  .contact__address {
    font-size: 17px; line-height: 1.3; margin-top: 14px;
  }
  .contact__list { list-style: none; margin-top: 14px; }
  .contact__item {
    display: flex; align-items: center; gap: 10px;
    font-size: 17px; line-height: 1; margin-bottom: 6px;
  }
  .contact__icon {
    width: 24px; height: 24px; border-radius: 50%;
    background: var(--orange); flex: none;
    display: flex; align-items: center; justify-content: center;
  }
  .partner {
    position: absolute; left: 430px; bottom: 92px;
    display: flex; align-items: center; gap: 8px; color: var(--navy);
  }
  .partner__dot {
    width: 24px; height: 24px; border-radius: 50%; background: var(--blue);
  }
  .partner__name { font-size: 15px; font-weight: 600; line-height: 1; }
  .partner__note { font-size: 9px; font-weight: 500; margin-top: 3px; }
</style>
</head>
<body>
<main class="sheet">

  <section class="card card--fr" lang="fr">
    <div class="brand">
      <div class="brand__mark"><span class="brand__dot"></span><span class="brand__name">Bintal</span></div>
      <p class="brand__school">Ecole Les Bintal</p>
    </div>
    <div class="card__divider"></div>
    <div class="contact">
      <p class="contact__name">Nom ici</p>
      <p class="contact__title">Titre ici</p>
      <p class="contact__address">Ligne d'adresse ici,<br>adressez les détails ici</p>
      <ul class="contact__list">
        <li class="contact__item"><span class="contact__icon"><svg width="14" height="14" viewBox="0 0 24 24"><path fill="#fff" d="M6.6 10.8a15 15 0 0 0 6.6 6.6l2.2-2.2c.3-.3.7-.4 1-.2 1.1.4 2.3.6 3.6.6.6 0 1 .4 1 1V20c0 .6-.4 1-1 1A17 17 0 0 1 3 4c0-.6.4-1 1-1h3.5c.6 0 1 .4 1 1 0 1.3.2 2.5.6 3.6.1.3 0 .7-.2 1z"/></svg></span>21 40 55 12</li>
        <li class="contact__item"><span class="contact__icon"><svg width="14" height="14" viewBox="0 0 24 24"><rect x="3" y="6" width="18" height="12" rx="1" fill="#fff"/><path d="M3 6l9 7 9-7" fill="none" stroke="#f26a21" stroke-width="1.6"/></svg></span>nom@ecolebintal.dz</li>
        <li class="contact__item"><span class="contact__icon"><svg width="14" height="14" viewBox="0 0 24 24" fill="none" stroke="#fff" stroke-width="1.8"><circle cx="12" cy="12" r="9"/><path d="M3 12h18M12 3c3 3 3 15 0 18M12 3c-3 3-3 15 0 18"/></svg></span>www.ecolebintal.dz</li>
      </ul>
    </div>
    <div class="partner">
      <span class="partner__dot"></span>
      <div><p class="partner__name">Halvorth Quenby</p><p class="partner__note">Approved Centre</p></div>
    </div>
    <div class="card__band"></div>
  </section>

  <section class="card card--en" lang="en">
    <div class="brand">
      <div class="brand__mark"><span class="brand__dot"></span><span class="brand__name">Bintal</span></div>
      <p class="brand__school">Bintal School</p>
    </div>
    <div class="card__divider"></div>
    <div class="contact">
      <p class="contact__name">Name Here</p>
      <p class="contact__title">Title Here</p>
      <p class="contact__address">Address line here,<br>address detials here</p>
      <ul class="contact__list">
        <li class="contact__item"><span class="contact__icon"><svg width="14" height="14" viewBox="0 0 24 24"><path fill="#fff" d="M6.6 10.8a15 15 0 0 0 6.6 6.6l2.2-2.2c.3-.3.7-.4 1-.2 1.1.4 2.3.6 3.6.6.6 0 1 .4 1 1V20c0 .6-.4 1-1 1A17 17 0 0 1 3 4c0-.6.4-1 1-1h3.5c.6 0 1 .4 1 1 0 1.3.2 2.5.6 3.6.1.3 0 .7-.2 1z"/></svg></span>21 40 55 12</li>
        <li class="contact__item"><span class="contact__icon"><svg width="14" height="14" viewBox="0 0 24 24"><rect x="3" y="6" width="18" height="12" rx="1" fill="#fff"/><path d="M3 6l9 7 9-7" fill="none" stroke="#f26a21" stroke-width="1.6"/></svg></span>name@bintalschool.dz</li>
        <li class="contact__item"><span class="contact__icon"><svg width="14" height="14" viewBox="0 0 24 24" fill="none" stroke="#fff" stroke-width="1.8"><circle cx="12" cy="12" r="9"/><path d="M3 12h18M12 3c3 3 3 15 0 18M12 3c-3 3-3 15 0 18"/></svg></span>www.bintalschool.dz</li>
      </ul>
    </div>
    <div class="partner">
      <span class="partner__dot"></span>
      <div><p class="partner__name">Halvorth Quenby</p><p class="partner__note">Approved Centre</p></div>
    </div>
    <div class="card__band"></div>
  </section>

</main>
</body>
</html>
```